Birch Flooring Supply

Basic one-sided business card design using the attached logo. Vintage americana theme. Font is modified Arial Nova Cond, but anything that coordinates can be used

```html
<!DOCTYPE html>
<html lang="en">
<head>
<meta charset="utf-8">
<title>Birch Flooring Supply – Business Card</title>
<link rel="stylesheet" href="https://fonts.googleapis.com/css2?family=Oswald:wght@300;400;600;700&display=swap">
<style>
  :root {
    --stage: #1d1d1f;
    --kraft: #b3916f;
    --kraft-dark: #a3805f;
    --card-black: #1b1b1b;
    --ink-white: #f4f1ec;
    --gold: #c49a6c;
    --muted: #e6e1da;
  }
  * { box-sizing: border-box; margin: 0; padding: 0; }
  html, body {
    width: 1200px; height: 689px; overflow: hidden;
    background: var(--stage);
    font-family: "Oswald", "Arial Narrow", sans-serif;
  }
  .stage {
    width: 1200px; height: 689px;
    display: flex; align-items: center; justify-content: center; gap: 50px;
  }
  .card {
    width: 525px; height: 300px; border-radius: 18px;
    position: relative; overflow: hidden;
  }
  .card--back {
    background: radial-gradient(circle at 30% 30%, var(--kraft), var(--kraft-dark));
    display: flex; align-items: center; justify-content: center;
  }
  .card--front {
    background: var(--card-black);
    display: flex; align-items: center;
  }
  .brand {
    width: 190px; height: 190px; border-radius: 50%;
    display: flex; flex-direction: column; align-items: center; justify-content: center;
    text-align: center; font-weight: 600; text-transform: uppercase;
    line-height: 1.05; letter-spacing: 1px;
  }
  .card--back .brand { border: 4px solid var(--ink-white); color: var(--ink-white); }
  .card--front .brand { border: 4px solid var(--gold); color: var(--ink-white); }
  .brand__main { font-size: 44px; }
  .brand__sub { font-size: 17px; letter-spacing: 2px; }
  .front__logo { width: 262px; display: flex; justify-content: center; }
  .front__divider { width: 1px; height: 190px; background: var(--ink-white); }
  .front__details { padding-left: 26px; color: var(--ink-white); }
  .person__name { font-size: 30px; font-weight: 700; text-transform: uppercase; letter-spacing: 1px; line-height: 1; }
  .person__title { font-size: 15px; font-weight: 400; color: var(--gold); margin: 4px 0 12px; }
  .contact { list-style: none; font-weight: 300; font-size: 13px; }
  .contact li { display: flex; align-items: flex-start; gap: 10px; line-height: 1.45; }
  .contact svg { width: 12px; height: 12px; margin-top: 4px; flex: none; fill: none; stroke: var(--muted); stroke-width: 1.6; }
</style>
</head>
<body>
<main class="stage">
  <section class="card card--back" aria-label="Card back">
    <div class="brand">
      <span class="brand__main">Birch</span>
      <span class="brand__sub">Flooring Supply</span>
    </div>
  </section>

  <section class="card card--front" aria-label="Card front">
    <div class="front__logo">
      <div class="brand">
        <span class="brand__main">Birch</span>
        <span class="brand__sub">Flooring Supply</span>
      </div>
    </div>
    <div class="front__divider"></div>
    <div class="front__details">
      <h1 class="person__name">Daniel Hart</h1>
      <p class="person__title">Founder &amp; CEO</p>
      <ul class="contact">
        <li><svg viewBox="0 0 12 12"><path d="M6 11 C3 7 2 5.5 2 4.2 A4 4 0 0 1 10 4.2 C10 5.5 9 7 6 11Z"/><circle cx="6" cy="4.3" r="1.3"/></svg><span>4821 Alder Lane<br>Fairview, CT 06400</span></li>
        <li><svg viewBox="0 0 12 12"><path d="M2 1.5 L4 1.5 L5 4 L3.7 5 A6 6 0 0 0 7 8.3 L8 7 L10.5 8 L10.5 10 A8.5 8.5 0 0 1 2 1.5Z"/></svg><span>555-210-4418</span></li>
        <li><svg viewBox="0 0 12 12"><rect x="3" y="1" width="6" height="10" rx="1"/><path d="M5.2 9.2h1.6"/></svg><span>555-382-7091</span></li>
        <li><svg viewBox="0 0 12 12"><rect x="1.5" y="5" width="9" height="4.5"/><path d="M3.5 5V1.5h5V5M3.5 9.5V11h5V9.5"/></svg><span>555-647-2953</span></li>
        <li><svg viewBox="0 0 12 12"><rect x="1" y="2.5" width="10" height="7"/><path d="M1 2.5 L6 6.5 L11 2.5"/></svg><span>info@birchflooringsupply.com</span></li>
        <li><svg viewBox="0 0 12 12"><circle cx="6" cy="6" r="4.8"/><path d="M1.2 6h9.6M6 1.2c-2.4 2.6-2.4 7 0 9.6M6 1.2c2.4 2.6 2.4 7 0 9.6"/></svg><span>birchflooringsupply.com</span></li>
      </ul>
    </div>
  </section>
</main>
</body>
</html>
```